Law Firm Website

We are looking to update our old, tired and very flat website. We have someone who will code and host the site but we need some design inspiration. The website will consist of no more than 2/3 pages, possibly with pop-ups for information. We already have all the blurb. We would like something distinctive, clean and eye-catching, using the purple and white theme that we already use on our firm stationery. Examples uploaded. Current website URL is www.dunmorewillett.example.

Industry/Entity Type

Law Firm

```html
<!DOCTYPE html>
<html lang="en">
<head>
<meta charset="utf-8">
<title>Dunmore + Willett Solicitors</title>
<link href="https://fonts.googleapis.com/css2?family=Crimson+Text:ital,wght@0,400;1,400;1,700&family=Noto+Sans:wght@400;700&family=Arimo:wght@400&display=swap" rel="stylesheet">
<style>
  :root {
    --purple: #573c8e;
    --purple-deep: #452a78;
    --purple-text: #3f2a82;
    --ink: #1f2630;
    --grey: #7a7a7a;
    --nav: #555555;
    --white: #ffffff;
    --night-top: #0f2a5a;
    --night-mid: #1d3f7a;
    --night-low: #0b1830;
  }
  * { margin: 0; padding: 0; box-sizing: border-box; }
  html, body { width: 1200px; height: 977px; overflow: hidden; background: var(--white); }
  .page { position: relative; width: 1200px; height: 977px; overflow: hidden; }

  .site-header { position: absolute; left: 0; top: 0; width: 1200px; height: 84px; background: var(--white); }
  .brand { position: absolute; left: 211px; top: 20px; color: var(--ink); font-family: "Noto Sans", sans-serif; font-weight: 700; }
  .brand-name { display: block; font-size: 25px; line-height: 28px; letter-spacing: -0.3px; }
  .brand-sub { display: block; font-size: 12px; line-height: 14px; margin-left: 44px; }

  .main-nav { position: absolute; left: 0; top: 0; height: 84px; font-family: "Arimo", Arial, sans-serif; font-size: 13px; }
  .main-nav a { position: absolute; top: 0; height: 84px; line-height: 86px; color: var(--nav); text-decoration: none; white-space: nowrap; }
  .main-nav a.is-active { background: var(--purple); color: var(--white); width: 61px; text-align: center; }

  .hero { position: absolute; left: 0; top: 84px; width: 1200px; height: 526px;
    background: linear-gradient(180deg, var(--night-top) 0%, var(--night-mid) 35%, #2b3f6a 58%, #3a3340 72%, var(--night-low) 100%); }
  .hero-caption { position: absolute; left: 426px; top: 205px; width: 482px; height: 126px; background: rgba(25, 30, 40, 0.72); padding: 26px 20px 0 21px; }
  .hero-title { font-family: "Crimson Text", serif; font-weight: 400; font-size: 20px; color: var(--white); line-height: 24px; }
  .hero-text { margin-top: 9px; font-family: "Noto Sans", sans-serif; font-size: 11px; line-height: 17px; color: #d8d8d8; }
  .hero-dots { position: absolute; top: 483px; left: 582px; display: flex; gap: 5px; }
  .hero-dots span { width: 9px; height: 9px; border-radius: 50%; background: #3a3f4a; }
  .hero-dots span.is-current { background: #d0d0d0; }

  .section-title { font-family: "Crimson Text", serif; font-weight: 400; font-size: 21px; line-height: 26px; color: #4a4a55; }
  .section-title em { font-style: normal; color: var(--purple-text); }

  .about { position: absolute; left: 212px; top: 640px; width: 452px; }
  .about-text { margin-top: 13px; font-family: "Noto Sans", sans-serif; font-size: 12px; line-height: 20.5px; color: var(--grey); }

  .divider { position: absolute; left: 686px; top: 642px; width: 2px; height: 128px; background: linear-gradient(180deg, rgba(0,0,0,0), rgba(0,0,0,0.08), rgba(0,0,0,0)); }

  .testimonials { position: absolute; left: 715px; top: 643px; width: 275px; }
  .testimonial-nav { position: absolute; right: 2px; top: 6px; }
  .testimonial-quote { margin-top: 12px; font-family: "Crimson Text", serif; font-style: italic; font-size: 13px; line-height: 17.5px; color: #666; }
  .testimonial-name { margin-top: 10px; font-family: "Crimson Text", serif; font-style: italic; font-weight: 700; font-size: 13px; color: var(--purple-text); }

  .site-footer { position: absolute; left: 0; top: 816px; width: 1200px; height: 126px; background: var(--purple); text-align: center; font-family: "Arimo", Arial, sans-serif; color: var(--white); }
  .social { position: absolute; left: 549px; top: 26px; display: flex; gap: 5px; }
  .social span { width: 22px; height: 22px; border-radius: 50%; background: var(--white); }
  .footer-nav, .footer-legal { position: absolute; left: 0; width: 1200px; text-align: center; }
  .footer-nav { top: 65px; font-size: 13px; }
  .footer-legal { top: 90px; font-size: 11.5px; }
  .footer-nav a, .footer-legal a { color: var(--white); text-decoration: none; }
  .sep { display: inline-block; margin: 0 11px; color: rgba(255,255,255,0.55); }
  .copyright { position: absolute; left: 0; top: 942px; width: 1200px; height: 35px; background: var(--purple-deep); color: var(--white); font-family: "Arimo", Arial, sans-serif; font-size: 11px; line-height: 35px; text-align: center; }
</style>
</head>
<body>
<div class="page">
  <header class="site-header">
    <div class="brand">
      <span class="brand-name">Dunmore + Willett</span>
      <span class="brand-sub">Solicitors</span>
    </div>
    <nav class="main-nav">
      <a class="is-active" href="#" style="left:547px">Home</a>
      <a href="#" style="left:624px">About Us</a>
      <a href="#" style="left:704px">Areas Of Expertise</a>
      <a href="#" style="left:841px">Our Team</a>
      <a href="#" style="left:924px">Contact Us</a>
    </nav>
  </header>

  <section class="hero" role="img" aria-label="Night photograph of a city waterfront skyline with lit towers reflected in a marina">
    <div class="hero-caption">
      <h1 class="hero-title">Lorem Ipsum Dollar Sit Ammet Ponto</h1>
      <p class="hero-text">This is Photoshop's version &nbsp;of Lorem Ipsum. Proin gravida nibh vel velit auctor aliquet. Aenean sollicitudin, lorem quis bibendum auctor, nisi elit consequat ipsum.</p>
    </div>
    <div class="hero-dots"><span class="is-current"></span><span></span><span></span></div>
  </section>

  <section class="about">
    <h2 class="section-title">About <em>Dunmore &amp; Willett Solicitors</em></h2>
    <p class="about-text">This is Photoshop's version &nbsp;of Lorem Ipsum. Proin gravida nibh vel velit auctor aliquet. Aenean sollicitudin, lorem quis bibendum auctor, nisi elit consequat ipsumiec sagittis sem nibh id elit. Duis sed odio sit amet nibh vulputate cursus a sit ametaur is. Mafrorbi accumsan ipsum velit. Nam nec tellus a odio.</p>
  </section>

  <div class="divider"></div>

  <section class="testimonials">
    <h2 class="section-title">Client's <em>Testimonials</em></h2>
    <svg class="testimonial-nav" width="14" height="10" viewBox="0 0 14 10" aria-label="Previous and next">
      <path d="M4 2 L1 5 L4 8" fill="none" stroke="#aaa" stroke-width="1.2"/>
      <path d="M9 2 L12 5 L9 8" fill="none" stroke="var(--purple-text)" stroke-width="1.4"/>
    </svg>
    <p class="testimonial-quote">Thank you so very much for all your efforts and dedications. You people are wonderfull. I will definitely refer to you if i needed your help again.</p>
    <p class="testimonial-name">Daniel R</p>
  </section>

  <footer class="site-footer">
    <div class="social"><span></span><span></span><span></span><span></span></div>
    <nav class="footer-nav">
      <a href="#">Home</a><span class="sep">|</span><a href="#">About Us</a><span class="sep">|</span><a href="#">Our Services</a><span class="sep">|</span><a href="#">Areas Of Experties</a><span class="sep">|</span><a href="#">Our Team</a><span class="sep">|</span><a href="#">Contact Us</a>
    </nav>
    <nav class="footer-legal">
      <a href="#">Privacy Policy</a><span class="sep">|</span><a href="#">Terms &amp; Conditions</a><span class="sep">|</span><a href="#">Sitemap</a>
    </nav>
  </footer>
  <div class="copyright">Copyright 2014 - All Rights Reserved</div>
</div>
</body>
</html>
```